Water ATM Card

Need a design for water ATM cards. Size of card is 3.375 x 2.125 inch
On the Front include the Cedar Brook Logo.
Bottom right corner should have Price $100
On the Back
This card is to be used to access water refills at any Cedar Brook Water Vending Machines.
Please contact (869) 415 2983 or (869) 238 4617 or email clearflowhub@mailbox-example.com for any assistance or recharging of card.

```html
<!DOCTYPE html>
<html lang="en">
<head>
<meta charset="UTF-8">
<title>Cedar Brook Water Card</title>
<link rel="stylesheet" href="https://fonts.googleapis.com/css2?family=Poppins:wght@400;600;700&display=swap">
<style>
  :root {
    --stage: #2f2f2f;
    --back-top: #1aa6e6;
    --back-bottom: #1550c4;
    --front-light: #e6f9ff;
    --front-mid: #b9eefc;
    --water-light: #3fd0f5;
    --water-deep: #0a7fd6;
    --brand-blue: #1d5aa6;
    --white: #ffffff;
    --rule: rgba(255,255,255,0.7);
  }
  * { margin: 0; padding: 0; box-sizing: border-box; }
  html, body { width: 1200px; height: 689px; overflow: hidden; }
  body {
    background: var(--stage);
    font-family: "Poppins", sans-serif;
    position: relative;
  }
  .card {
    position: absolute;
    top: 181px;
    width: 520px;
    height: 327px;
    border-radius: 22px;
    overflow: hidden;
  }
  .card-back {
    left: 50px;
    background: linear-gradient(160deg, var(--back-top) 0%, var(--back-bottom) 100%);
    color: var(--white);
    text-align: center;
    padding: 34px 36px 0;
  }
  .back-statement {
    font-weight: 700;
    font-size: 19px;
    line-height: 1.3;
    text-transform: uppercase;
    letter-spacing: 0.3px;
  }
  .contact-divider {
    display: flex;
    align-items: center;
    gap: 12px;
    margin: 22px 0 8px;
  }
  .contact-divider .rule { flex: 1; height: 1px; background: var(--rule); }
  .contact-divider .label { font-weight: 600; font-size: 14px; }
  .phone-line { font-weight: 600; font-size: 27px; line-height: 1.25; white-space: nowrap; }
  .phone-line .joiner { font-weight: 400; font-size: 15px; margin: 0 4px; }
  .email-line { font-weight: 700; font-size: 20px; line-height: 1.4; white-space: nowrap; }
  .email-line .joiner { font-weight: 400; font-size: 15px; margin-right: 6px; }
  .assist-line { font-weight: 400; font-size: 15px; margin-top: 2px; }

  .card-front {
    left: 630px;
    background: linear-gradient(120deg, var(--front-light) 0%, var(--front-mid) 100%);
  }
  .water-area { position: absolute; inset: 0; width: 100%; height: 100%; }
  .brand {
    position: absolute;
    left: 40px;
    top: 140px;
    display: flex;
    align-items: center;
    gap: 12px;
  }
  .brand-dot {
    width: 22px; height: 22px; border-radius: 50%;
    background: var(--brand-blue);
  }
  .brand-name {
    font-weight: 700;
    font-size: 32px;
    color: var(--brand-blue);
    text-transform: uppercase;
    letter-spacing: 1px;
  }
  .price {
    position: absolute;
    right: 26px;
    bottom: 20px;
    font-weight: 700;
    font-size: 22px;
    color: var(--white);
    letter-spacing: 0.5px;
  }
</style>
</head>
<body>
  <section class="card card-back">
    <p class="back-statement">This card is to be used to access water refills at any Cedar Brook water vending machines</p>
    <div class="contact-divider">
      <span class="rule"></span><span class="label">Please contact</span><span class="rule"></span>
    </div>
    <p class="phone-line">(869) 415 2983<span class="joiner">or</span>(869) 238 4617</p>
    <p class="email-line"><span class="joiner">or</span>clearflowhub@mailbox-example.com</p>
    <p class="assist-line">for any assistance or recharging of card</p>
  </section>

  <section class="card card-front">
    <svg class="water-area" viewBox="0 0 520 327" role="img" aria-label="Photo of a clear blue water wave with bubbles rising from the lower left to the upper right">
      <defs>
        <linearGradient id="waterFill" x1="0" y1="0" x2="1" y2="1">
          <stop offset="0" stop-color="#3fd0f5"/>
          <stop offset="1" stop-color="#0a7fd6"/>
        </linearGradient>
      </defs>
      <path d="M120 327 C210 300 250 250 290 170 C320 105 360 80 420 70 C470 60 500 45 520 40 L520 327 Z" fill="url(#waterFill)"/>
    </svg>
    <div class="brand">
      <span class="brand-dot"></span>
      <span class="brand-name">Cedar Brook</span>
    </div>
    <p class="price">Price $100</p>
  </section>
</body>
</html>
```